Essential Oil 15ml - package of 6

Design of a box of 6 different essential oils.
+ design of the bottle stickers
My bottles are 15ml clear blue glass.

The pictures attached are my competitors...

Target Market(s)

BRAMBLEWICK USA

Font styles to use
Serif

Requirements
Must have
• Our logo + "essential oil" and type (lavender, eucalyptus etc....)
• 15ml - 0.50 fl.oz.
• special color for the oil type.

```html
<!DOCTYPE html>
<html lang="en">
<head>
<meta charset="utf-8">
<title>Sela Grove Essential Oils – Bottle Labels</title>
<link href="https://fonts.googleapis.com/css2?family=Lato:wght@400;700;900&display=swap" rel="stylesheet">
<style>
  :root {
    --backdrop: #8e8e8e;
    --lavender: #8a2b8e;
    --eucalyptus: #2b97aa;
    --peppermint: #1f8a3b;
    --orange: #c78b22;
    --gold: #d8b04a;
    --gold-dark: #9c7420;
    --ink: #ffffff;
    --ink-soft: rgba(255, 255, 255, 0.45);
  }
  * { box-sizing: border-box; margin: 0; padding: 0; }
  html, body {
    width: 1200px;
    height: 646px;
    overflow: hidden;
    background: var(--backdrop);
    font-family: "Lato", sans-serif;
  }
  .canvas {
    position: relative;
    width: 1200px;
    height: 646px;
  }
  .label {
    position: absolute;
    top: 334px;
    width: 102px;
    height: 128px;
    color: var(--ink);
    text-align: center;
    border-top: 3px solid var(--gold);
    border-bottom: 3px solid var(--gold);
    box-shadow: 0 -1px 0 var(--gold-dark), 0 1px 0 var(--gold-dark);
  }
  .label--large {
    top: 332px;
    width: 110px;
    height: 134px;
  }
  .label--lavender { background: var(--lavender); }
  .label--eucalyptus { background: var(--eucalyptus); }
  .label--peppermint { background: var(--peppermint); }
  .label--orange { background: var(--orange); }
  .brand-mark {
    display: block;
    width: 18px;
    height: 18px;
    margin: 6px auto 0;
    border-radius: 50%;
    background: var(--ink);
  }
  .brand-name {
    margin-top: 6px;
    font-size: 12.5px;
    font-weight: 700;
    letter-spacing: 0.1px;
  }
  .product-line {
    margin-top: 3px;
    font-size: 10px;
    color: var(--ink-soft);
  }
  .oil-type {
    display: inline-block;
    margin-top: 8px;
    padding: 2px 0 1px;
    font-size: 11.5px;
    font-weight: 700;
    letter-spacing: 0.4px;
    border-top: 1px solid var(--ink);
    border-bottom: 1px solid var(--ink);
  }
  .volume {
    position: absolute;
    left: 0;
    right: 0;
    bottom: 10px;
    font-size: 5px;
    color: var(--ink);
    opacity: 0.85;
  }
</style>
</head>
<body>
<main class="canvas">
  <section class="label label--lavender" style="left:101px">
    <span class="brand-mark"></span>
    <p class="brand-name">Sela Grove</p>
    <p class="product-line">Essential Oils</p>
    <p class="oil-type">LAVANDA</p>
    <p class="volume">0.5 fl. Oz (15ml)</p>
  </section>
  <section class="label label--eucalyptus" style="left:208px">
    <span class="brand-mark"></span>
    <p class="brand-name">Sela Grove</p>
    <p class="product-line">Essential Oils</p>
    <p class="oil-type">EUCALYPTUS</p>
    <p class="volume">0.5 fl. Oz (15ml)</p>
  </section>
  <section class="label label--large label--eucalyptus" style="left:321px">
    <span class="brand-mark"></span>
    <p class="brand-name">Sela Grove</p>
    <p class="product-line">Essential Oils</p>
    <p class="oil-type">EUCALYPTUS</p>
    <p class="volume">0.5 fl. Oz (15ml)</p>
  </section>
  <section class="label label--large label--peppermint" style="left:475px">
    <span class="brand-mark"></span>
    <p class="brand-name">Sela Grove</p>
    <p class="product-line">Essential Oils</p>
    <p class="oil-type">PEPPERMINT</p>
    <p class="volume">0.5 fl. Oz (15ml)</p>
  </section>
  <section class="label label--large label--lavender" style="left:630px">
    <span class="brand-mark"></span>
    <p class="brand-name">Sela Grove</p>
    <p class="product-line">Essential Oils</p>
    <p class="oil-type">LAVANDA</p>
    <p class="volume">0.5 fl. Oz (15ml)</p>
  </section>
  <section class="label label--large label--orange" style="left:784px">
    <span class="brand-mark"></span>
    <p class="brand-name">Sela Grove</p>
    <p class="product-line">Essential Oils</p>
    <p class="oil-type">ORANGE</p>
    <p class="volume">0.5 fl. Oz (15ml)</p>
  </section>
  <section class="label label--peppermint" style="left:901px">
    <span class="brand-mark"></span>
    <p class="brand-name">Sela Grove</p>
    <p class="product-line">Essential Oils</p>
    <p class="oil-type">PEPPERMINT</p>
    <p class="volume">0.5 fl. Oz (15ml)</p>
  </section>
  <section class="label label--orange" style="left:1013px">
    <span class="brand-mark"></span>
    <p class="brand-name">Sela Grove</p>
    <p class="product-line">Essential Oils</p>
    <p class="oil-type">ORANGE</p>
    <p class="volume">0.5 fl. Oz (15ml)</p>
  </section>
</main>
</body>
</html>
```